Roll up/retractable banner for trade show - higher education software company

My company, BrightQuill Scholastics, will be attending a trade show soon, and we need a design for a "roll up" or "retractable" banner. According to the printer, it must be exactly 33 inches wide by 81 inches tall, at a DPI of 150 (not 300).

This is the exact product from Zorvena: https://zrvn.example/8Kq2LmPx

The banner should have a professional feel and have a similar aesthetic to our brochure, web site, etc. Please see attached files. Use as much or as little as you see fit from the attached files. If you use stock photos in your design, just let me know where I need to go to purchase them.

Our software company focuses on advising and student success for colleges and universities. I like the idea of focusing on the "use cases" of our software, rather than specific software offerings, but I am open to interpretations.

Website: https://brightquillscholastics.example

REQUIREMENT
The final product MUST be in a file format which I can edit later on, with elements in different layers. Either Photoshop or GIMP will be fine, though I can also load .ai files. GIMP is actually preferred, but not required. Mainly, I must be able to alter text, move graphics around, swap out graphics, etc, as needed in the future. If you only work with psd and ai, please provide both file versions in the end.

Target Market(s)

University staff / VP's / presidents / decision-makers at trade shows and conferences

Industry/Entity Type

Higher Education / Software Development

Font styles to use
Sans Serif
Other font styles liked:
• MONTSERRAT is the font used in my logo and brochure, I use RALEWAY on the website. But these are not requirements-- Use what you think looks best.

Requirements
Must have
• 33"wide by 81" tall, 150 DPI. Professional appearance. Final files must be PSD, AI, or GIMP format so I can edit/tweak text and images later if needed. If using AI, please provide both .ai and .psd files.
Nice to have
• Similar wording/content/graphics/colors & fonts as brochure and website (see attached files). Especially some of the use-case wording from the brochure. Flashy and important information should be at the top of the banner, because if this is placed behind a table in a booth, info on the bottom might be obscured or hidden. The QR code from the brochure might be nice to have as well.

```html
<!DOCTYPE html>
<html lang="en">
<head>
<meta charset="utf-8">
<title>BrightQuill Scholastics – Retractable Banner</title>
<link rel="stylesheet" href="https://fonts.googleapis.com/css2?family=Montserrat:wght@400;500;600;700;800&display=swap">
<style>
  :root {
    --page-bg: #eceeef;
    --paper: #ffffff;
    --pink: #d63f84;
    --orange: #f28c1e;
    --blue: #2a9fd8;
    --navy: #1f3a6b;
    --ink: #3a3a3a;
    --muted: #5c5c5c;
  }
  * { box-sizing: border-box; margin: 0; padding: 0; }
  html, body { width: 1200px; height: 848px; overflow: hidden; }
  body {
    background: var(--page-bg);
    font-family: "Montserrat", Arial, sans-serif;
    color: var(--ink);
    position: relative;
  }
  .banner {
    position: absolute;
    left: 435px; top: 19px;
    width: 330px; height: 810px;
    background: var(--paper);
    box-shadow: 0 2px 10px rgba(0,0,0,.18);
    overflow: hidden;
  }
  /* Header */
  .brand-header {
    position: absolute; top: 0; left: 0; right: 0; height: 80px;
  }
  .brand-mark {
    position: absolute; left: 22px; top: 28px; width: 135px;
    display: flex; align-items: center; gap: 7px;
  }
  .brand-mark .dot {
    flex: 0 0 14px; width: 14px; height: 14px; background: var(--pink);
  }
  .brand-mark .name {
    font-weight: 800; font-size: 10px; line-height: 1.15; color: var(--navy);
    letter-spacing: .2px;
  }
  .contact {
    position: absolute; left: 168px; top: 22px; width: 150px;
    font-size: 5.6px; line-height: 1.5; color: var(--ink);
    white-space: nowrap;
  }
  .contact .company { font-weight: 800; font-size: 7px; color: var(--navy); }
  .contact .company span { color: var(--orange); }
  .contact .label { font-weight: 700; color: var(--pink); }
  .contact b { font-weight: 700; }
  .intro {
    position: absolute; left: 22px; right: 20px; top: 80px;
    font-size: 6.3px; line-height: 1.45; color: var(--ink);
  }
  .intro .question { font-weight: 700; color: var(--navy); }
  .intro .accent { color: var(--pink); }
  /* Pink message band */
  .message-band {
    position: absolute; left: 0; right: 0; top: 135px; height: 57px;
    background: var(--pink);
    display: flex; align-items: center; justify-content: center;
    text-align: center;
    color: #fff; font-weight: 700; font-size: 11.5px; line-height: 1.3;
  }
  /* Hero photo */
  .hero-photo {
    position: absolute; left: 0; right: 0; top: 192px; height: 254px;
    background: linear-gradient(120deg, #c9c4bd 0%, #8e7f6c 35%, #5b6a82 60%, #b6aa98 100%);
  }
  .hero-curve {
    position: absolute; left: 0; top: 330px; width: 330px; height: 130px;
  }
  .device-lineup {
    position: absolute; left: 62px; top: 366px; width: 206px; height: 120px;
    background: linear-gradient(180deg, #f2f4f6, #d5dbe1);
    border-radius: 4px;
  }
  /* Product section */
  .product-heading {
    position: absolute; left: 0; right: 0; top: 497px;
    text-align: center; font-weight: 800; font-size: 11px; line-height: 1.25;
    color: var(--navy);
  }
  .product-heading span { display: block; color: var(--orange); }
  .features {
    position: absolute; left: 40px; right: 30px; top: 540px;
    display: grid; grid-template-columns: 1fr 1fr; column-gap: 16px; row-gap: 11px;
  }
  .feature h3 { font-size: 5.6px; font-weight: 700; color: var(--navy); margin-bottom: 2px; }
  .feature p { font-size: 4.8px; line-height: 1.5; color: var(--muted); }
  /* Footer band */
  .footer-wave {
    position: absolute; left: 0; top: 700px; width: 330px; height: 40px;
  }
  .footer-band {
    position: absolute; left: 0; right: 0; top: 728px; bottom: 0;
    background: var(--blue);
    text-align: center; color: #fff;
    padding-top: 4px;
  }
  .footer-band .use-cases {
    font-weight: 700; font-size: 11.5px; line-height: 1.2; text-transform: uppercase;
  }
  .footer-band .tagline {
    font-weight: 500; font-size: 8px; margin-top: 6px;
  }
</style>
</head>
<body>
  <main class="banner">
    <header class="brand-header">
      <div class="brand-mark">
        <span class="dot"></span>
        <span class="name">BrightQuill<br>Scholastics</span>
      </div>
      <div class="contact">
        <div class="company">BRIGHTQUILL <span>SCHOLASTICS</span></div>
        <div><span class="label">CALL US :</span> 555-014-2270</div>
        <div><b>email:</b> info@brightquillscholastics.example</div>
        <div><b>web:</b> brightquillscholastics.example</div>
      </div>
    </header>

    <p class="intro">
      <span class="question">What is BrightQuill?</span><br>
      BrightQuill is an <span class="accent">open source</span>, web-based academic advising and degree audit platform, with added functionality to make it a complete Enterprise-Level Student Success Management System. Its unique design makes advising students and achieving student success easier than ever before.
    </p>

    <section class="message-band">
      <p>We are happy to customize<br>and custom program solutions to fit your needs</p>
    </section>

    <div class="hero-photo" role="img" aria-label="Photo of an advisor and a student reviewing work together at a laptop"></div>

    <svg class="hero-curve" viewBox="0 0 330 130" aria-hidden="true">
      <path d="M0 70 C90 20 200 10 330 40 L330 130 L0 130 Z" fill="var(--orange)"/>
      <path d="M0 88 C100 40 210 30 330 55 L330 130 L0 130 Z" fill="var(--pink)"/>
      <path d="M0 95 C100 48 210 40 330 62 L330 130 L0 130 Z" fill="var(--paper)"/>
    </svg>

    <div class="device-lineup" role="img" aria-label="Software screens shown on a desktop monitor, laptop, tablet and phone"></div>

    <h2 class="product-heading">ENTERPRISE-LEVEL STUDENT<span>SUCCESS MANAGEMENT SYSTEM</span></h2>

    <section class="features">
      <article class="feature">
        <h3>Hosting</h3>
        <p>Your BrightQuill installation is hosted on our secure cloud servers, with daily backups and constant uptime monitoring included.</p>
      </article>
      <article class="feature">
        <h3>Training</h3>
        <p>Through BrightQuill's onboarding sessions, your advisors and staff learn every feature at their own pace with live help.</p>
      </article>
      <article class="feature">
        <h3>Support</h3>
        <p>BrightQuill installations are handled by the experts who built it. Our team answers questions quickly and knows your campus needs.</p>
      </article>
      <article class="feature">
        <h3>Custom Programming</h3>
        <p>We are ready to build new tools on request. Tell us your workflow and we will shape the platform around it.</p>
      </article>
      <article class="feature">
        <h3>Data Storage</h3>
        <p>Student data stays in your hands. Records are encrypted and stored in one place, ready for secure reporting.</p>
      </article>
      <article class="feature">
        <h3>Security</h3>
        <p>We take security seriously at every level, with regular audits, role-based access and full compliance with privacy rules.</p>
      </article>
    </section>

    <svg class="footer-wave" viewBox="0 0 330 40" aria-hidden="true">
      <path d="M0 18 C110 -2 220 2 330 22 L330 40 L0 40 Z" fill="var(--pink)"/>
      <path d="M0 26 C110 8 220 10 330 28 L330 40 L0 40 Z" fill="var(--blue)"/>
    </svg>
    <footer class="footer-band">
      <p class="use-cases">Academic Advising<br>Early Alerts Text Messaging<br>Appointments &amp; More</p>
      <p class="tagline">Student Success has never been so intuitive and powerful</p>
    </footer>
  </main>
</body>
</html>
```